依頼詳細
現在、不動産業務にて空家・空地・相続させたお客様へお手紙と返信用ハガキをつけお送りしています。使用していますはがきデザインはワードで作成し、プリンターではがきに印刷しお手紙に添えてお送りしています。
返信いただくお客様に、
該当する内容に〇をつけていただき、送っていただいております。(2パターン使用中です)
お客様からの返信率はあまりない状況です。

※お客様の年齢層の幅も広いですし、相続対象者の方にもお送りしますので、お客様の中に はDMはがき自体を不快に思われる方もいらっしゃいますので、
デザインはシンプルなもので字体やバランスなどのご提案も含めお願いしたいです。
記載項目
裏面:ご回答書(ご所有の不動産について)、ご意見・ご要望、お客様のご住所・
お名前・ご連絡先
希望イメージ
シンプル 複雑
単色 カラフル
暗い 明るい
日常 高級
遊び心 厳粛
未来的 伝統的
女性的 男性的
希望する色
納品ファイル
• 高解像度JPG (.jpg)
• PNG形式 (.png)
補足説明
■ 選んだ理由

提案していただきありがとうございました。
見た瞬間から目を引かれるデザインで、柔らかい雰囲気がとても気に入りました。

■ 提案者全員のお礼・コメント

素晴らしいデザインでした!
ありがとうございました。

```html
<!DOCTYPE html>
<html lang="ja">
<head>
<meta charset="UTF-8">
<title>ご所有の不動産についてお聞かせください</title>
<link rel="stylesheet" href="https://fonts.googleapis.com/css2?family=Noto+Sans+JP:wght@400;500;700&display=swap">
<style>
  :root {
    --ink: #2b2b2b;
    --muted: #444;
    --band-light: #e6e6e6;
    --band-dark: #4a4a4a;
    --line: #555;
    --label-bg: #e8e8e8;
    --paper: #ffffff;
  }
  * { margin: 0; padding: 0; box-sizing: border-box; }
  html, body { width: 809px; height: 1200px; overflow: hidden; background: var(--paper); }
  body { font-family: "Noto Sans JP", sans-serif; color: var(--ink); position: relative; }

  .survey-header {
    position: absolute; left: 22px; top: 0; width: 787px; height: 112px;
    background: var(--band-light);
  }
  .survey-title {
    position: absolute; left: 40px; top: 30px;
    font-size: 39px; font-weight: 700; letter-spacing: 0.5px; white-space: nowrap;
  }
  .survey-subtitle {
    position: absolute; left: 0; top: 98px; width: 809px; text-align: center;
    font-size: 27px; font-weight: 700;
  }
  .house-mark {
    position: absolute; left: 690px; top: 80px; width: 100px; height: 105px;
    background: linear-gradient(180deg, #d0d0d0, #9a9a9a); border-radius: 6px;
  }

  .notes { position: absolute; left: 128px; top: 180px; font-size: 19px; line-height: 33px; color: var(--muted); }
  .notes .tick { display: inline-block; vertical-align: -6px; }

  .options { position: absolute; left: 128px; top: 258px; list-style: none; }
  .option {
    display: flex; align-items: center; height: 58px;
    font-size: 30px; font-weight: 500;
  }
  .option .box {
    width: 28px; height: 28px; border: 2px solid var(--line); margin-right: 22px; flex: none;
  }

  .comment-frame { position: absolute; left: 92px; top: 730px; }

  .thanks-band {
    position: absolute; left: 22px; top: 866px; width: 765px; height: 60px;
    background: var(--band-dark); border-radius: 8px 8px 0 0;
    color: #fff; font-size: 33px; font-weight: 700; text-align: center; line-height: 60px;
  }

  .contact-table {
    position: absolute; left: 22px; top: 944px; width: 765px;
    border-collapse: collapse;
  }
  .contact-table th, .contact-table td { border: 2px solid var(--line); }
  .contact-table th {
    width: 112px; background: var(--label-bg);
    font-size: 19px; font-weight: 700; text-align: center;
  }
  .contact-table td { position: relative; }
  .row-name { height: 96px; }
  .row-address { height: 80px; }
  .row-phone { height: 80px; }
  .furigana { position: absolute; left: 14px; top: 4px; font-size: 13px; color: var(--muted); }
  .furigana-rule { position: absolute; left: 0; right: 0; top: 26px; border-top: 1px dashed #999; }
</style>
</head>
<body>
  <header>
    <div class="survey-header">
      <h1 class="survey-title">ご所有の不動産についてお聞かせください</h1>
    </div>
    <p class="survey-subtitle">– アンケート –</p>
    <div class="house-mark" role="img" aria-label="家のイラスト"></div>
  </header>

  <div class="notes">
    <p>※該当する項目に
      <svg class="tick" width="26" height="26" viewBox="0 0 26 26"><rect x="2" y="6" width="16" height="16" fill="none" stroke="#444" stroke-width="2"/><path d="M6 13 L11 19 L23 3" fill="none" stroke="#222" stroke-width="3"/></svg>
      チェックをいれてください。</p>
    <p>※お預かりした個人情報は本件の目的以外には使用いたしません。</p>
  </div>

  <ul class="options">
    <li class="option"><span class="box"></span>売却してもよい</li>
    <li class="option"><span class="box"></span>売却するつもりはない</li>
    <li class="option"><span class="box"></span>どちらとも決めていない</li>
    <li class="option"><span class="box"></span>不動産の価格を知りたい</li>
    <li class="option"><span class="box"></span>当分様子をみて決める</li>
    <li class="option"><span class="box"></span>将来自分（子供）が家を建てて住む予定</li>
    <li class="option"><span class="box"></span>不動産の活用を考えている</li>
    <li class="option"><span class="box"></span>その他</li>
  </ul>

  <svg class="comment-frame" width="640" height="112" viewBox="0 0 640 112" aria-hidden="true">
    <path d="M250 4 H30 Q4 4 4 30 V82 Q4 108 30 108 H250" fill="none" stroke="#555" stroke-width="3"/>
    <path d="M390 4 H610 Q636 4 636 30 V82 Q636 108 610 108 H390" fill="none" stroke="#555" stroke-width="3"/>
  </svg>

  <div class="thanks-band">ご回答ありがとうございました</div>

  <table class="contact-table">
    <tr class="row-name"><th>お名前</th><td><span class="furigana">ふりがな</span><span class="furigana-rule"></span></td></tr>
    <tr class="row-address"><th>ご住所</th><td></td></tr>
    <tr class="row-phone"><th>ご連絡先</th><td></td></tr>
  </table>
</body>
</html>
```